Kalmoret Windham & Associates

We would like a simple, professional business card using a similar font to our logo.

Industry/Entity Type

Law Firm

Contact Information for Business Card

Martin Kalmoret, Esq. 47 Tillman Lane, 2nd Floor Brantwick, MA 02490 Office: 781.555.0143 Cell: 508.555.0196 Email: marty@kwfirmma.com kalmoretwindhamlaw.com

Font styles to use
Other font styles liked:
• We would like to use the fonts used in the logo or similar

Colors
0054AA
0677BA
7BADD7
CADEEF
E8F1F8

Requirements
Must have
• We would like the fonts to match the logo
Nice to have
• not too much design- very simple and professional business card. I added a picture of a business card that I tried to start but I am not a designer! Hopefully it will help with the address and phone numbers and kind of what we are looking for.

```html
<!DOCTYPE html>
<html lang="en">
<head>
<meta charset="utf-8">
<title>Kalmoret Windham &amp; Associates – Business Cards</title>
<link rel="stylesheet" href="https://fonts.googleapis.com/css2?family=Cinzel:wght@600;700&family=Cormorant+Garamond:wght@600&family=Montserrat:wght@400;500&display=swap">
<style>
  :root {
    --backdrop: #a3a3a3;
    --card: #ffffff;
    --navy: #152f6b;
    --blue: #0677ba;
    --bright: #1d8fdc;
    --pale: #e8f1f8;
    --gold: #c9a24a;
    --ink: #2b2b2b;
  }
  * { box-sizing: border-box; margin: 0; padding: 0; }
  html, body { width: 686px; height: 1200px; overflow: hidden; }
  body { background: var(--backdrop); position: relative; font-family: "Montserrat", Arial, sans-serif; }

  .card {
    position: absolute; left: 39px; width: 608px; height: 350px;
    background: var(--card); overflow: hidden;
    box-shadow: 0 2px 6px rgba(0,0,0,.25);
  }
  .card--one { top: 40px; }
  .card--two { top: 430px; }
  .card--three { top: 820px; }

  .texture {
    position: absolute; inset: 0;
    background: radial-gradient(ellipse at 30% 40%, #f4f6f9 0%, #ffffff 70%);
  }
  .texture--gold {
    background: linear-gradient(135deg, rgba(201,162,74,.10) 0%, rgba(255,255,255,0) 40%, rgba(201,162,74,.12) 100%);
  }
  .accents { position: absolute; inset: 0; }

  .firm {
    position: absolute; left: 0; right: 0; top: 46px;
    display: flex; justify-content: center; align-items: center; gap: 14px;
  }
  .firm__square { width: 74px; height: 74px; background: var(--navy); }
  .firm__name {
    font-family: "Cinzel", Georgia, serif; font-weight: 700; color: var(--navy);
    text-transform: uppercase; line-height: 1.02; font-size: 23px; letter-spacing: .5px;
  }
  .firm__name small { display: block; font-size: 14px; letter-spacing: 1px; }

  .person {
    position: absolute; left: 0; right: 0; top: 160px; text-align: center;
    font-family: "Cinzel", Georgia, serif; font-weight: 600; font-size: 20px;
    color: var(--navy); letter-spacing: .5px;
  }
  .person__suffix {
    font-family: "Cormorant Garamond", Georgia, serif; font-weight: 600;
    font-size: 19px; letter-spacing: 0;
  }
  .card--three .person { top: 196px; }

  .contact {
    position: absolute; left: 0; right: 0; top: 212px; text-align: center;
    font-style: normal; font-size: 11.5px; line-height: 1.6; color: var(--ink);
  }
  .contact--band { top: 266px; color: #ffffff; }
  .band {
    position: absolute; left: 0; right: 0; bottom: 0; height: 100px; background: var(--navy);
  }
</style>
</head>
<body>

<section class="card card--one">
  <div class="texture" role="img" aria-label="Faint grey curved line texture"></div>
  <svg class="accents" viewBox="0 0 608 350" aria-hidden="true">
    <polygon points="0,322 608,322 608,330 0,330" fill="var(--bright)"/>
    <polygon points="0,332 300,332 270,350 0,350" fill="var(--navy)"/>
    <polygon points="300,332 608,332 608,350 270,350" fill="var(--blue)"/>
    <polygon points="0,300 180,300 150,322 0,322" fill="var(--navy)"/>
  </svg>
  <div class="firm">
    <div class="firm__square"></div>
    <div class="firm__name">Kalmoret<br>Windham<small>&amp; Associates</small></div>
  </div>
  <p class="person">MARTIN KALMORET, <span class="person__suffix">Esq.</span></p>
  <address class="contact">
    47 Tillman Lane, 2nd Floor Brantwick, MA 02490<br>
    Office: 781.555.0143 &nbsp;|&nbsp; Cell: 508.555.0196<br>
    Email: marty@kwfirmma.com &nbsp;|&nbsp; kalmoretwindhamlaw.com
  </address>
</section>

<section class="card card--two">
  <div class="texture" role="img" aria-label="Faint grey curved line texture"></div>
  <svg class="accents" viewBox="0 0 608 350" aria-hidden="true">
    <polygon points="540,0 608,0 608,80" fill="var(--navy)"/>
    <polygon points="508,0 530,0 608,92 608,118" fill="var(--bright)"/>
    <polygon points="0,200 60,260 0,320" fill="var(--navy)"/>
    <polygon points="0,176 84,260 0,344 0,330 70,260 0,190" fill="var(--bright)"/>
    <polygon points="608,300 608,350 540,350" fill="#d9dde3"/>
  </svg>
  <div class="firm">
    <div class="firm__square"></div>
    <div class="firm__name">Kalmoret<br>Windham<small>&amp; Associates</small></div>
  </div>
  <p class="person">MARTIN KALMORET, <span class="person__suffix">Esq.</span></p>
  <address class="contact">
    47 Tillman Lane, 2nd Floor Brantwick, MA 02490<br>
    Office: 781.555.0143 &nbsp;|&nbsp; Cell: 508.555.0196<br>
    Email: marty@kwfirmma.com &nbsp;|&nbsp; kalmoretwindhamlaw.com
  </address>
</section>

<section class="card card--three">
  <div class="texture texture--gold" role="img" aria-label="Gold geometric line ornament"></div>
  <div class="band"></div>
  <svg class="accents" viewBox="0 0 608 350" aria-hidden="true">
    <line x1="0" y1="250" x2="608" y2="250" stroke="var(--gold)" stroke-width="2"/>
  </svg>
  <div class="firm">
    <div class="firm__square"></div>
    <div class="firm__name">Kalmoret<br>Windham<small>&amp; Associates</small></div>
  </div>
  <p class="person">MARTIN KALMORET, <span class="person__suffix">Esq.</span></p>
  <address class="contact contact--band">
    47 Tillman Lane, 2nd Floor Brantwick, MA 02490<br>
    Office: 781.555.0143 &nbsp;|&nbsp; Cell: 508.555.0196<br>
    Email: marty@kwfirmma.com &nbsp;|&nbsp; kalmoretwindhamlaw.com
  </address>
</section>

</body>
</html>
```